新しくオープンしたラーメン居酒屋の新メニューのチラシ制作をお願いします。
こだわりが強く、比較的高級なラーメン屋です。高級感のある本格的なデザイン、訴求力がありながらも上品なデザインを希望します。
サイズ:A4サイズ
ノビテルで入稿します。
編集できるイラストレーターとPDFファイルでの納品をお願いします。

イメージ通りでした。

この度はたくさんのご応募ありがとうございます。今後ともよろしくお願いいたします。

```html
<!DOCTYPE html>
<html lang="ja">
<head>
<meta charset="utf-8">
<title>冷製 鯛出汁塩山椒そば</title>
<link rel="stylesheet" href="https://fonts.googleapis.com/css2?family=Shippori+Mincho:wght@400;500;600&display=swap">
<style>
  :root {
    --paper: #ffffff;
    --ink: #1a1a1a;
    --accent-teal: #3a8fa6;
    --bowl-light: #f7b870;
    --bowl-mid: #ec8a2c;
    --bowl-deep: #c9641a;
    --badge-bg: #111111;
    --badge-text: #ffffff;
  }
  * { margin: 0; padding: 0; box-sizing: border-box; }
  html, body { width: 855px; height: 1200px; overflow: hidden; background: var(--paper); }
  .flyer {
    position: relative;
    width: 855px;
    height: 1200px;
    background: var(--paper);
    font-family: "Shippori Mincho", serif;
    color: var(--ink);
  }
  .season-label {
    position: absolute;
    top: 106px;
    left: 0; right: 0;
    text-align: center;
    font-size: 34px;
    letter-spacing: 0.12em;
    color: var(--accent-teal);
    font-weight: 400;
  }
  .menu-title {
    position: absolute;
    top: 180px;
    left: 0; right: 0;
    text-align: center;
    font-size: 54px;
    font-weight: 500;
    letter-spacing: 0.1em;
  }
  .dish-photo {
    position: absolute;
    left: 226px;
    top: 326px;
    width: 404px;
    height: 404px;
  }
  .price {
    position: absolute;
    left: 650px;
    top: 760px;
    font-size: 38px;
    letter-spacing: 0.03em;
  }
  .description {
    position: absolute;
    top: 898px;
    left: 0; right: 0;
    text-align: center;
    font-size: 23px;
    line-height: 43px;
    letter-spacing: 0.05em;
  }
  .badge {
    position: absolute;
    left: 342px;
    top: 1049px;
    width: 171px;
    height: 68px;
    background: var(--badge-bg);
    color: var(--badge-text);
    display: flex;
    align-items: center;
    justify-content: center;
    font-size: 19px;
    letter-spacing: 0.08em;
  }
</style>
</head>
<body>
  <main class="flyer">
    <p class="season-label">夏季限定</p>
    <h1 class="menu-title">冷製 鯛出汁塩山椒そば</h1>

    <svg class="dish-photo" viewBox="0 0 404 404" role="img" aria-label="橙色の器に盛られた冷製鯛出汁塩山椒そばの写真">
      <defs>
        <radialGradient id="bowl-tone" cx="45%" cy="40%" r="60%">
          <stop offset="0%" stop-color="var(--bowl-light)"/>
          <stop offset="65%" stop-color="var(--bowl-mid)"/>
          <stop offset="100%" stop-color="var(--bowl-deep)"/>
        </radialGradient>
      </defs>
      <circle cx="202" cy="202" r="200" fill="url(#bowl-tone)"/>
    </svg>

    <p class="price">¥1,000</p>

    <p class="description">
      濃密ながら澄らかな真鯛出汁、<br>
      香りの異なる2種類の山椒を漬け込んだ香味油、<br>
      自家製の塩だれが三位一体となった一杯。
    </p>

    <div class="badge">化学調味料不使用</div>
  </main>
</body>
</html>
```